Website for vegan focused blog

A website is needed so that I can launch my new blog in Dubai. It will be mainly vegan focused but also lifestyle based. Wordpress based- i started to build a site on Wordpress but design is not my forte ;)
Main content on the site will be; my recipes, reviews of products/restaurants, lifestyle posts and travel.
For this I ask for a homepage design, a recipe design page that includes a recipe card and a generic page for posts that can show pictures and videos. Also a contact me page.
Main headers should be: Home, Recipes and happy for suggestions.
Must look clean and neat but appealing, happy for minimalist look. I like pink and grey colours. Must be Wordpress compatible.
Have attached a couple of example posts for reference
Must have social links etc.
name of blog is: Marnie on the dunes
Other blogs I like are: https://tidyskillet.example/ https://shebrightens.example/ https://shebrightens.example/ https://www.ohladycakes.com/https://figsforsupper.example/ https://tessaborlow.example/

Target Market(s)

Residents in the UAE. General individuals interested in vegan meals, plant based nutrition, travel and reviews.

Number of Pages Required

4 page

Colors
eea4c8
eda3c7
f9d9e8
dbdbdb
aaaaaa
d5d5d5

Requirements
Must have
• Recipe page- must include recipe card plug in option
• Social media integration
• Email sign ups

```html
<!DOCTYPE html>
<html lang="en">
<head>
<meta charset="utf-8">
<title>Marnie on the dunes — Mushroom Steak</title>
<link href="https://fonts.googleapis.com/css2?family=Lato:ital,wght@0,400;0,700;1,400&family=Playfair+Display:ital,wght@0,400;1,400&display=swap" rel="stylesheet">
<style>
  :root {
    --pink: #eea4c8;
    --pink-strong: #e989b6;
    --pink-soft: #f9d9e8;
    --line: #dbdbdb;
    --line-soft: #e8e8e8;
    --grey: #aaaaaa;
    --text: #444444;
    --ink: #333333;
    --white: #ffffff;
    --food-a: #3a4a2a;
    --food-b: #6b3a2a;
    --food-c: #c9583f;
  }
  * { box-sizing: border-box; margin: 0; padding: 0; }
  html, body { width: 1200px; height: 1200px; overflow: hidden; background: var(--white); }
  body { position: relative; font-family: "Lato", sans-serif; color: var(--text); }
  .abs { position: absolute; }

  .brand { left: 0; width: 1200px; top: 40px; text-align: center;
    font-family: "Playfair Display", serif; font-style: italic; font-size: 36px; color: var(--pink); }

  .nav { left: 0; top: 114px; width: 1200px; height: 38px; border-top: 1px solid var(--line); border-bottom: 1px solid var(--line); }
  .nav-item { top: 11px; font-family: "Playfair Display", serif; font-style: italic; font-size: 12px; color: var(--ink); transform: translateX(-50%); letter-spacing: .3px; }
  .search { left: 954px; top: 12px; }

  .dropdown { left: 617px; top: 154px; width: 111px; height: 74px; background: var(--white); border: 1px solid var(--line-soft); box-shadow: 0 2px 6px rgba(0,0,0,.06); z-index: 3; }
  .dropdown div { height: 24.5px; line-height: 24.5px; text-align: center; border-bottom: 1px solid var(--line-soft);
    font-family: "Playfair Display", serif; font-style: italic; font-size: 11px; color: var(--ink); }
  .dropdown div:last-child { border-bottom: 0; }

  .post-head { left: 234px; width: 506px; text-align: center; }
  .kicker { font-size: 7px; letter-spacing: .8px; text-transform: uppercase; color: var(--pink); }
  .post-title { font-family: "Playfair Display", serif; font-size: 19px; color: var(--pink); }
  .rule { width: 27px; height: 1px; background: var(--ink); margin: 0 auto; }
  .date { font-size: 7px; letter-spacing: .6px; color: #666; text-transform: uppercase; }

  .photo { background: linear-gradient(120deg, var(--food-a) 0%, var(--food-b) 45%, var(--food-c) 70%, #efe9e2 100%); }
  .hero { left: 234px; top: 275px; width: 506px; height: 352px; }

  .body-copy { left: 234px; width: 506px; font-size: 9.2px; line-height: 15px; color: var(--text); }

  .meta { left: 234px; top: 845px; width: 506px; height: 39px; border-top: 1px solid var(--line); border-bottom: 1px solid var(--line); }
  .meta-count { left: 0; top: 14px; font-size: 7px; color: var(--ink); }
  .meta-sep { left: 75px; top: 0; width: 1px; height: 38px; background: var(--line); }
  .meta-tags { left: 93px; top: 14px; font-size: 7px; color: var(--ink); }
  .meta-tags em { color: var(--grey); font-size: 7.5px; }
  .meta-social { right: 0; top: 15px; display: flex; gap: 10px; }
  .dot { width: 8px; height: 8px; border-radius: 50%; background: var(--ink); }

  .card { width: 241px; text-align: center; }
  .card .photo { height: 177px; }
  .card .kicker { margin-top: 15px; }
  .card-title { font-family: "Playfair Display", serif; font-size: 14px; line-height: 19px; color: var(--pink); margin-top: 7px; }
  .card .rule { margin-top: 13px; }

  .widget { left: 778px; width: 188px; border: 1px solid var(--line); padding: 0 12px; }
  .widget-title { font-family: "Playfair Display", serif; font-style: italic; font-size: 12px; color: var(--pink); position: absolute; left: 11px; }
  .social-row { position: absolute; left: 22px; top: 48px; display: flex; gap: 10px; }
  .social-row span { width: 20px; height: 20px; border-radius: 50%; background: var(--pink); display: block; }
  .about-photo { position: absolute; left: 11px; top: 47px; width: 164px; height: 96px; background: linear-gradient(180deg, #c7a58f 0%, #6f7e8a 55%, #2f3438 100%); }
  .about-text { position: absolute; left: 11px; top: 156px; width: 164px; text-align: center; font-size: 8px; line-height: 12.5px; color: var(--ink); }
  .more { position: absolute; left: 0; width: 186px; top: 222px; text-align: center; font-family: "Playfair Display", serif; font-style: italic; font-size: 8px; color: var(--ink); }
  .input { position: absolute; left: 11px; top: 47px; width: 164px; height: 30px; border: 1px solid var(--line); font-size: 7.5px; font-style: italic; color: #bbb; padding: 11px 10px; }
  .btn { position: absolute; left: 11px; width: 164px; background: var(--pink-soft); color: var(--white); text-align: center; }
  .btn-sub { top: 90px; height: 27px; line-height: 27px; font-size: 7px; letter-spacing: .8px; }
  .btn-feed { top: 308px; height: 26px; line-height: 26px; font-family: "Playfair Display", serif; font-style: italic; font-size: 8.5px; }
  .feed-grid { position: absolute; left: 11px; top: 47px; display: grid; grid-template-columns: 80px 80px; gap: 4px; }
  .feed-grid .photo { height: 80px; }
  .latest-thumb { position: absolute; left: 11px; top: 47px; width: 55px; height: 55px; }
  .latest-title { position: absolute; left: 79px; top: 51px; width: 104px; font-family: "Playfair Display", serif; font-style: italic; font-size: 7.5px; line-height: 11px; color: var(--ink); }
  .latest-cat { position: absolute; left: 79px; top: 80px; font-size: 6px; letter-spacing: .6px; color: #666; }
</style>
</head>
<body>

<header>
  <div class="abs brand">Marnie on the dunes</div>
  <nav class="abs nav">
    <span class="abs nav-item" style="left:444px">Home</span>
    <span class="abs nav-item" style="left:518px">About me</span>
    <span class="abs nav-item" style="left:598px">Recipes</span>
    <span class="abs nav-item" style="left:674px">Lifestyle</span>
    <span class="abs nav-item" style="left:751px">Contact</span>
    <svg class="abs search" width="12" height="12" viewBox="0 0 12 12" aria-label="Search">
      <circle cx="5" cy="5" r="3.8" fill="none" stroke="#333" stroke-width="1.5"/>
      <line x1="7.8" y1="7.8" x2="11" y2="11" stroke="#333" stroke-width="1.6"/>
    </svg>
  </nav>
  <div class="abs dropdown">
    <div>Travel</div><div>Reviews</div><div>Fitness</div>
  </div>
</header>

<main>
  <div class="abs post-head" style="top:180px"><div class="kicker">Food &amp; Drink</div></div>
  <h1 class="abs post-head post-title" style="top:198px;font-weight:400">Mushroom Steak</h1>
  <div class="abs post-head" style="top:233px"><div class="rule"></div></div>
  <div class="abs post-head date" style="top:246px">Saturday, September 8, 2018</div>

  <div class="abs photo hero" role="img" aria-label="Grilled portobello mushroom steak with roasted tomatoes, steamed spinach and a creamy dip"></div>

  <p class="abs body-copy" style="top:648px">Steak and vegan don't go in the same sentence BUT trust me on this...a decent sized Portobello shroom cooked just right with a blend of delicious marinade, it has the meatiest texture and its delicious as well oh and did we mention it is completely cruelty free!?</p>
  <p class="abs body-copy" style="top:708px">To get the right texture you need the right tools so I always suggest cooking this on a griddle pan or even on the BBQ to give it that additional boost of flavours.</p>
  <p class="abs body-copy" style="top:753px">When my non vegan friends are looking for something to cook when they have the plant powered team over for dinner, I always use this as a suggestion. The sides can be mixed and matched so in this instance I have used a grilled tomato and a pile of steamed spinach but you can add fries or salad or anything else that would be served alongside a steak. So all in all, it is a very versatile dish.</p>

  <div class="abs meta">
    <span class="abs meta-count">12 COMMENTS</span>
    <span class="abs meta-sep"></span>
    <span class="abs meta-tags">TAGGED : <em>Food, mushroom, balsamic vinegar, olive oil, cumin, paprika, spinach</em></span>
    <div class="abs meta-social"><span class="dot"></span><span class="dot"></span><span class="dot"></span><span class="dot"></span><span class="dot"></span></div>
  </div>

  <article class="abs card" style="left:234px;top:933px">
    <div class="photo" role="img" aria-label="Mushroom steak plate with tomatoes and spinach"></div>
    <div class="kicker">Lifestyle</div>
    <div class="card-title">Lorem ipsum dolor sit amet consectetur elit</div>
    <div class="rule"></div>
  </article>
  <article class="abs card" style="left:499px;top:933px">
    <div class="photo" role="img" aria-label="Mushroom steak plate with tomatoes and spinach"></div>
    <div class="kicker">Travel</div>
    <div class="card-title">Lorem ipsum dolor sit amet consectetur elit</div>
    <div class="rule"></div>
  </article>
</main>

<aside>
  <section class="abs widget" style="top:182px;height:94px">
    <h3 class="widget-title" style="top:17px;font-weight:400">Subscribe &amp; Follow</h3>
    <div class="social-row"><span></span><span></span><span></span><span></span><span></span></div>
  </section>

  <section class="abs widget" style="top:301px;height:243px">
    <h3 class="widget-title" style="top:19px;font-weight:400">About Marnie on the dunes</h3>
    <div class="about-photo" role="img" aria-label="Person standing on a beach at sunset beside a rocky headland"></div>
    <p class="about-text">On Marnie on the dunes, I share some delicious recipes either my own or from other fabulous sites that I have come across, my meal plans, reviews of products and restaurants that I visit and more.</p>
    <div class="more">More &#8594;</div>
  </section>

  <section class="abs widget" style="top:569px;height:142px">
    <h3 class="widget-title" style="top:17px;font-weight:400">Newsletter</h3>
    <div class="input">Your Email Address</div>
    <div class="btn btn-sub">SUBSCRIBE</div>
  </section>

  <section class="abs widget" style="top:737px;height:349px">
    <h3 class="widget-title" style="top:17px;font-weight:400">Snapshots</h3>
    <div class="feed-grid">
      <div class="photo" role="img" aria-label="Mushroom steak dish"></div>
      <div class="photo" role="img" aria-label="Mushroom steak dish"></div>
      <div class="photo" role="img" aria-label="Mushroom steak dish"></div>
      <div class="photo" role="img" aria-label="Mushroom steak dish"></div>
      <div class="photo" role="img" aria-label="Mushroom steak dish"></div>
      <div class="photo" role="img" aria-label="Mushroom steak dish"></div>
    </div>
    <div class="btn btn-feed">Follow on Snapshots &#8594;</div>
  </section>

  <section class="abs widget" style="top:1110px;height:120px">
    <h3 class="widget-title" style="top:17px;font-weight:400">Latest posts</h3>
    <div class="photo latest-thumb" role="img" aria-label="Mushroom steak dish"></div>
    <div class="latest-title">Maecenas sodales dignissim liberoid sodales</div>
    <div class="latest-cat">LIFESTYLE</div>
  </section>
</aside>

</body>
</html>
```